Remodel Flyer for realtors

"T" Ridgeline Builders

4"x 9" rack card front and back

www.BrambleworkHomes.example

555-318-4726

Let us fix what your home inspector finds!

Send us your inspection summary.

We are a licensed and Insured contractor.
CRC8071943

Serving
Marion County and Pelham Hollow

This flyer will sit in realtor offices for realtors to give to there buyers and sellers.

Target Market(s)

Realtors

Industry/Entity Type

Construction

Colors

Designer to choose colors to be used in the design.

```html
<!DOCTYPE html>
<html lang="en">
<head>
<meta charset="utf-8">
<title>T Ridgeline Builders – Rack Card</title>
<link href="https://fonts.googleapis.com/css2?family=Russo+One&family=Roboto:wght@300;400;500;700&display=swap" rel="stylesheet">
<style>
  :root {
    --orange: #f0900f;
    --dark: #464646;
    --ink: #2e2e2e;
    --white: #ffffff;
    --footer-grey: #ededed;
    --page: #e4e4e4;
  }
  * { box-sizing: border-box; margin: 0; padding: 0; }
  html, body { width: 1200px; height: 1200px; overflow: hidden; background: var(--page); }
  body { position: relative; font-family: "Roboto", sans-serif; color: var(--ink); }

  .rack-card {
    position: absolute;
    top: 125px;
    width: 422px;
    height: 949px;
    background: var(--white);
    overflow: hidden;
    box-shadow: 0 6px 18px rgba(0,0,0,0.18);
  }
  .rack-card--front { left: 132px; }
  .rack-card--back { left: 646px; }

  /* ---------- Front ---------- */
  .brand {
    position: absolute;
    top: 38px; left: 0; width: 100%;
    text-align: center;
  }
  .brand__mark {
    width: 62px; height: 62px;
    margin: 0 auto 18px;
    background: var(--orange);
  }
  .brand__name {
    font-family: "Roboto", sans-serif;
    font-weight: 500;
    color: var(--dark);
    font-size: 22px;
    letter-spacing: 1px;
    line-height: 1;
  }
  .brand__name span {
    display: block;
    font-size: 12px;
    letter-spacing: 9px;
    margin-top: 8px;
    padding-left: 9px;
  }

  .photo {
    position: absolute;
  }
  .photo--living {
    left: 0; top: 555px; width: 422px; height: 232px;
    background: linear-gradient(180deg, #d9c6a4 0%, #c99a68 55%, #b9652e 100%);
  }
  .front-frame {
    position: absolute; left: 0; top: 186px;
    width: 422px; height: 412px;
  }
  .photo--bedroom {
    left: 26px; top: 239px; width: 368px; height: 305px;
    border-radius: 46px;
    background: linear-gradient(180deg, #ede5d6 0%, #d9cdb7 50%, #b9a488 100%);
  }

  .tagline {
    position: absolute;
    left: 0; top: 787px; width: 422px; height: 99px;
    background: var(--orange);
    border-radius: 0 10px 10px 0;
    display: flex; align-items: center; justify-content: center;
    text-align: center;
    font-family: "Russo One", sans-serif;
    color: var(--white);
    font-size: 25px;
    line-height: 30px;
  }
  .front-url {
    position: absolute;
    left: 0; top: 905px; width: 100%;
    text-align: center;
    font-size: 13px;
    letter-spacing: 3.4px;
    color: var(--ink);
  }

  /* ---------- Back ---------- */
  .back-hero {
    position: absolute; left: 0; top: 0;
    width: 422px; height: 305px;
  }
  .photo--lounge {
    left: 46px; top: 0; width: 376px; height: 257px;
    border-radius: 0 0 10px 72px;
    background: linear-gradient(180deg, #e9d9c2 0%, #dcc7a8 45%, #b97a45 100%);
  }

  .about {
    position: absolute; left: 41px; top: 330px; width: 360px;
  }
  .section-title {
    font-family: "Russo One", sans-serif;
    font-size: 21px;
    line-height: 26px;
  }
  .section-title--about { color: var(--orange); }
  .section-title--about em { font-style: normal; color: var(--dark); }
  .about p {
    font-weight: 300;
    font-size: 13.4px;
    line-height: 16px;
    margin-top: 14px;
  }
  .about p + p { margin-top: 15px; }

  .services {
    position: absolute; left: 0; top: 489px;
    width: 422px; height: 237px;
    background: var(--orange);
    padding: 14px 28px 0 41px;
    color: var(--white);
  }
  .services .section-title { color: var(--white); }
  .services p {
    margin-top: 5px;
    font-weight: 300;
    font-size: 13.2px;
    line-height: 15.9px;
    text-align: justify;
  }

  .cta {
    position: absolute; left: 29px; top: 706px;
    width: 366px; height: 47px;
    border-radius: 24px;
    background: var(--dark);
    color: var(--white);
    font-weight: 700;
    font-size: 16.5px;
    letter-spacing: 0.4px;
    display: flex; align-items: center; justify-content: center;
  }

  .license {
    position: absolute; left: 0; top: 766px; width: 100%;
    text-align: center;
    color: var(--orange);
  }
  .license__note { font-weight: 700; font-size: 14px; letter-spacing: 0.3px; }
  .license__number {
    font-family: "Russo One", sans-serif;
    font-size: 25px;
    margin-top: 4px;
    letter-spacing: 0.5px;
  }

  .contact {
    position: absolute; left: 0; top: 829px;
    width: 422px; height: 120px;
    background: var(--footer-grey);
    text-align: center;
    padding-top: 26px;
    font-size: 14px;
    line-height: 23px;
    color: var(--ink);
  }
</style>
</head>
<body>

  <section class="rack-card rack-card--front">
    <div class="brand">
      <div class="brand__mark"></div>
      <div class="brand__name">T RIDGELINE<span>BUILDERS</span></div>
    </div>

    <div class="photo photo--living" role="img" aria-label="Photo of a bright living room with fireplace, white sofas and hardwood floor"></div>

    <svg class="front-frame" viewBox="0 0 422 412" width="422" height="412" aria-hidden="true">
      <path d="M0,95 Q0,5 90,5 L340,5 Q422,5 422,75 L422,120 L400,120 L400,294 L422,294 L422,330 Q422,398 340,404 L130,404 Q0,404 0,330 Z"
            fill="#464646" stroke="#ffffff" stroke-width="6"/>
      <rect x="18" y="44" width="384" height="324" rx="54" fill="#ffffff"/>
    </svg>

    <div class="photo photo--bedroom" role="img" aria-label="Photo of a furnished bedroom with tray ceiling and large windows"></div>

    <div class="tagline">LET US FIX WHAT YOUR<br>HOME INSPECTOR FINDS!</div>
    <div class="front-url">www.BrambleworkHomes.example</div>
  </section>

  <section class="rack-card rack-card--back">
    <svg class="back-hero" viewBox="0 0 422 305" width="422" height="305" aria-hidden="true">
      <path d="M0,0 L422,0 L422,290 Q400,292 380,292 L120,305 Q0,305 0,185 Z" fill="#464646"/>
      <path d="M38,0 L422,0 L422,265 L118,267 Q38,267 38,187 Z" fill="#ffffff"/>
    </svg>
    <div class="photo photo--lounge" role="img" aria-label="Photo of a spacious modern lounge with sectional sofa and spiral staircase"></div>

    <div class="about">
      <h2 class="section-title section-title--about">About <em>Us</em></h2>
      <p>Whether it's getting your home remodeled or fixing damage that's been done to your home, we're here to help you every step of the way.</p>
      <p>"T" Ridgeline Builders has been around since 1976, so we really mean it when we say we're here to help you.</p>
    </div>

    <div class="services">
      <h2 class="section-title">Our Services</h2>
      <p>Residential or Commercial We've got all your needs covered: from residential remodels, to commercial damage repairs and everything in between. Don't hesitate to ask us a question or inquire as to why a certain process has to take place. All of our staff are friendly and knowledgeable because we know what it's like to be in your shoes. We want you to know just how special you and your project are to us, so we do our very best to ensure that you and your needs always come first. We even have a complimentary estimate where we'll come out to you!</p>
    </div>

    <div class="cta">Send us your inspection summary.</div>

    <div class="license">
      <div class="license__note">We are a licensed and Insured contractor.</div>
      <div class="license__number">CRC8071943</div>
    </div>

    <div class="contact">
      218 Larkspur Ave, Fenwick, Florida 30000, United States<br>
      555-318-4726 &nbsp;|&nbsp; dana@brambleworkhomes.example<br>
      www.brambleworkhomes.example
    </div>
  </section>

</body>
</html>
```